Mortgage Broking boutique Business

I’m wanting a revamped look to my existing business card design. I do like the black and silver but happy to have other colours introduced based on your creation. I’ve attached a copy of my current card so you can have a starting point updated details noted brloe. I deal with high net worth individuals so need my card to be sophisticated, classy that gives off a classy vibe

Target Market(s)

High net worth, wealthy

Industry/Entity Type

Mortgage Brokerage

Contact Information for Business Card

Job title: Finance Executive
Phone: +61 7 3862 1197
Mobile: 0431 275 506
Email: marcus@quillbrookcapital.com.au
Web: www.quillbrookcapital.com.au
Address: level 22 Tamberlin House, 48 Mercer Rd Brisbane QLD 4000

Font styles to use
Other font styles liked:
• Helvetica

Colors

Designer to choose colors to be used in the design.

Requirements
Must have
• Use my existing card design as a starting point

```html
<!DOCTYPE html>
<html lang="en">
<head>
<meta charset="utf-8">
<title>Quillbrook Capital — Business Card</title>
<link href="https://fonts.googleapis.com/css2?family=Arimo:wght@400;700&display=swap" rel="stylesheet">
<style>
  :root {
    --backdrop: #2a2c30;
    --card-black: #0d0d0d;
    --card-white: #f2f2f2;
    --ink: #111111;
    --ink-soft: #333333;
    --silver: #e6e6e6;
    --font: "Arimo", Helvetica, Arial, sans-serif;
  }
  * { box-sizing: border-box; margin: 0; padding: 0; }
  html, body {
    width: 1200px; height: 900px; overflow: hidden;
    background: var(--backdrop);
    font-family: var(--font);
  }
  .canvas {
    position: relative; width: 1200px; height: 900px;
    display: flex; align-items: center; justify-content: center; gap: 48px;
  }
  .card {
    position: relative; width: 510px; height: 292px;
    border-radius: 22px; overflow: hidden;
    box-shadow: 0 18px 40px rgba(0,0,0,.45);
  }

  /* Back: contact side */
  .card-back { background: var(--card-white); color: var(--ink); }
  .holder { position: absolute; left: 34px; top: 32px; }
  .holder-name { font-size: 21px; font-weight: 700; letter-spacing: .3px; white-space: nowrap; }
  .holder-title { font-size: 13px; color: var(--ink-soft); margin-top: 3px; }
  .contact-list { position: absolute; left: 34px; top: 106px; list-style: none; }
  .contact-list li {
    display: flex; align-items: center; gap: 9px;
    font-size: 12.5px; line-height: 23px; color: var(--ink);
    white-space: nowrap;
  }
  .contact-list svg { width: 12px; height: 12px; flex: none; }
  .brand-tag { position: absolute; right: 0; top: 40px; }
  .brand-tag-name {
    font-size: 15px; font-weight: 700; letter-spacing: 2.5px;
    padding: 0 24px 0 14px; white-space: nowrap;
  }
  .brand-tag-rule { display: block; height: 1.5px; background: var(--ink); margin-top: 6px; }
  .brand-tag-rule + .brand-tag-rule { margin-top: 4px; margin-left: 14px; }

  /* Front: brand side */
  .card-front { background: var(--card-black); color: var(--silver); }
  .frame-outer {
    position: absolute; inset: 24px; border: 1.5px solid var(--silver);
  }
  .frame-inner {
    position: absolute; inset: 30px; border: 1.5px solid var(--silver);
  }
  .wordmark {
    position: absolute; inset: 0;
    display: flex; flex-direction: column; align-items: center; justify-content: center;
    color: var(--silver);
  }
  .wordmark-main { font-size: 30px; font-weight: 700; letter-spacing: 9px; padding-left: 9px; }
  .wordmark-sub { font-size: 14px; font-weight: 400; letter-spacing: 3px; padding-left: 3px; margin-top: 2px; }
</style>
</head>
<body>
<main class="canvas">

  <section class="card card-back" aria-label="Business card contact side">
    <div class="holder">
      <h1 class="holder-name">MARCUS REID</h1>
      <p class="holder-title">Finance Executive</p>
    </div>

    <ul class="contact-list">
      <li>
        <svg viewBox="0 0 12 12" aria-hidden="true"><path d="M3.5 1 L1.5 2.5 C1.5 7 5 10.5 9.5 10.5 L11 8.5 L8.5 7 L7.3 8 C5.8 7.3 4.7 6.2 4 4.7 L5 3.5 Z" fill="#111"/></svg>
        0431 275 506
      </li>
      <li>
        <svg viewBox="0 0 12 12" aria-hidden="true"><rect x="1" y="3" width="10" height="7" rx="1.5" fill="#111"/><path d="M2.5 4 C4 1 8 1 9.5 4" stroke="#111" stroke-width="1.4" fill="none"/></svg>
        +61 7 3862 1197
      </li>
      <li>
        <svg viewBox="0 0 12 12" aria-hidden="true"><rect x="1" y="2.5" width="10" height="7" fill="#111"/><path d="M1 2.5 L6 6.5 L11 2.5" stroke="#f2f2f2" stroke-width="1" fill="none"/></svg>
        marcus@quillbrookcapital.com.au
      </li>
      <li>
        <svg viewBox="0 0 12 12" aria-hidden="true"><circle cx="6" cy="6" r="5" fill="#111"/><path d="M1 6 H11 M6 1 C3.5 4 3.5 8 6 11 M6 1 C8.5 4 8.5 8 6 11" stroke="#f2f2f2" stroke-width=".8" fill="none"/></svg>
        www.quillbrookcapital.com.au
      </li>
      <li>
        <svg viewBox="0 0 12 12" aria-hidden="true"><path d="M6 11.5 C3 8 2 6.5 2 4.8 A4 4 0 0 1 10 4.8 C10 6.5 9 8 6 11.5 Z" fill="#111"/><circle cx="6" cy="4.8" r="1.4" fill="#f2f2f2"/></svg>
        level 22 Tamberlin House, 48 Mercer Rd Brisbane QLD 4000
      </li>
    </ul>

    <div class="brand-tag">
      <p class="brand-tag-name">QUILLBROOK.CAPITAL</p>
      <span class="brand-tag-rule"></span>
      <span class="brand-tag-rule"></span>
    </div>
  </section>

  <section class="card card-front" aria-label="Business card brand side">
    <div class="frame-outer"></div>
    <div class="frame-inner"></div>
    <div class="wordmark">
      <span class="wordmark-main">QUILLBROOK</span>
      <span class="wordmark-sub">CAPITAL</span>
    </div>
  </section>

</main>
</body>
</html>
```